Business Card Design Project

Dunmore Freightwerk is an IT focussed, forward thinking online uniform and inventory management company supplying into large scale Defence, Emergency Services and Government Department contracts.

Our logo is our name, however we have adopted the use of a globe (see attached) within a recent promotional DVD and would like this worked into the design.

We are wanting something sharp and sophisticated.

Requirements
Must have
• Space for QR Code
Website details www.dunmorefreightwerk.example
Nice to have
• 2 sided - name/logo only on rear side.

```html
<!DOCTYPE html>
<html lang="en">
<head>
<meta charset="utf-8">
<title>Dunmore Freightwerk — Business Card</title>
<link rel="stylesheet" href="https://fonts.googleapis.com/css2?family=Cinzel:wght@400&family=Arimo:wght@700&display=swap">
<style>
  :root {
    --stage: #ececec;
    --card: #000000;
    --ink: #ffffff;
    --silver-light: #e9edf3;
    --silver-mid: #8d96a3;
    --silver-dark: #2a2e35;
    --glow: #3b5bd6;
  }
  * { margin: 0; padding: 0; box-sizing: border-box; }
  html, body {
    width: 1200px;
    height: 900px;
    overflow: hidden;
    background: var(--stage);
  }
  .card {
    position: absolute;
    top: 265px;
    width: 548px;
    height: 352px;
    background: var(--card);
    overflow: hidden;
  }
  .card--front { left: 39px; }
  .card--back { left: 617px; }

  .website {
    position: absolute;
    left: 28px;
    top: 38px;
    font-family: "Arimo", Arial, sans-serif;
    font-weight: 700;
    font-size: 18px;
    color: var(--ink);
  }

  .globe {
    position: absolute;
    background:
      radial-gradient(circle at 50% 42%, var(--silver-light) 0%, var(--silver-mid) 28%, var(--silver-dark) 44%, transparent 46%),
      radial-gradient(ellipse 50% 9% at 50% 92%, var(--glow) 0%, rgba(59,91,214,0.35) 55%, transparent 100%);
  }
  .globe--front {
    left: 256px;
    top: 148px;
    width: 300px;
    height: 200px;
    background:
      radial-gradient(circle 77px at 185px 84px, var(--silver-light) 0%, var(--silver-mid) 55%, var(--silver-dark) 92%, transparent 100%),
      radial-gradient(ellipse 130px 16px at 185px 178px, var(--glow) 0%, rgba(59,91,214,0.35) 55%, transparent 100%);
  }
  .globe--back {
    left: 170px;
    top: 36px;
    width: 220px;
    height: 190px;
    background:
      radial-gradient(circle 77px at 105px 77px, var(--silver-light) 0%, var(--silver-mid) 55%, var(--silver-dark) 92%, transparent 100%),
      radial-gradient(ellipse 100px 14px at 105px 170px, var(--glow) 0%, rgba(59,91,214,0.35) 55%, transparent 100%);
  }

  .brand-name {
    position: absolute;
    left: 0;
    right: 0;
    top: 226px;
    text-align: center;
    font-family: "Cinzel", "Times New Roman", serif;
    font-weight: 400;
    font-size: 24px;
    letter-spacing: 3px;
    color: var(--ink);
  }
</style>
</head>
<body>
  <section class="card card--front" aria-label="Business card front">
    <p class="website">www.dunmorefreightwerk.example</p>
    <div class="globe globe--front" role="img" aria-label="Silver wireframe globe resting on a blue glow"></div>
  </section>

  <section class="card card--back" aria-label="Business card back">
    <div class="globe globe--back" role="img" aria-label="Silver wireframe globe resting on a blue glow"></div>
    <p class="brand-name">DUNMORE FREIGHTWERK</p>
  </section>
</body>
</html>
```